Growing Wellness Company Needs an Amazing Cover for a series of Booklets

We are publishing our own series of booklets on health & wellness topics, called Vital Spark Primers and need an inspiring, modern design for the cover. We are beginning with the Title Diabetes: Type 2, but we will use this design for other titles later one.

SIZE:
This will be the front and back of a 8.5 x 5.5 booklet, plus 2 sample interior pages.

COLOR:
We are an industry leaders and prefer touse vibrant colors and designs to inspire our clients to change to a healthier lifestyle.

REQUIREMENTS:
I am attaching our Vital Spark logo, which needs to be on each cover, but does not need to be the focal point. You may you the words vital spark or just the b logo. The topic/title needs to be no lower than 1/2" from the top of the cover.

I'm attaching some samples of items I like, but please be creative!
If you would like to see some of our other in-house samples of publications send me a message and I'll show you. I will give detailed feedback so dive in and get creative!

FRONT COVER: 
1. Can you please make sure the title is in the top 1.5" of the page, i can't tell from this view. 
Type 2 Diabetes (1st line, bigger) 
A Simple Guide to Understanding & Controlling Your Blood Sugar (Second Row, much smaller) this can also be below the 1.5" line if it needs to be. 
3.We would like to see three shapes maybe toward the bottom with these words in them, one word per shape. inspire, equip, succeed 

IMAGE 
1. We would like you to leave a placeholder for an image, but would like to see different shapes, such as a rounded square or rectangle or a rectangle with two square corners and two rounded corners. 
2. Please play with some different border options as well,

BACKSIDE 
1. please put our information on the back side on the bottom, small. the information i will put in a file on the brief, the 2nd page has our address, phone, etc. 
2. Add our TA logo (attached as an image in the design brief)

Thanks! looking forward to what else you have. 

Reason: I want to give more time to get more/better designs in, i know this is a little more involved project.

Reason: Still not happy with designs, would like to see more.

Hello - thank you for submitting designs, the designs are getting a little too busy....here is a website I love the simplicity of...thanks!  http://www.brightmeadowcare.example   

Reason: We are getting closer to narrowing it down, I want to give the designers a few more days to tweak their designs, then i will ask the final 2 or 3 to submit a couple version of the inside pages. I will supply text for those so you know what you're working with. Thanks!

Target Market(s)

Our clients are adults, about 50/50 men & women in the age range from 20-70 with most being in their early 50's. from high school education up to professional degrees

Font styles to use
Serif
Sans Serif
Script

Colors
a64599
e34197
00a98f
9bcb3c
ffc214
f78f20
f37122
0492cd
6a439a

Requirements
Must have
• Eye catching, inspiring design that entices people to read our booklet:

I need a front and back cover and 2 interior page samples , we will be using more of an info graphic style inside possible with a few actual photographs

FRONT COVER REQUIREMENTS:
Title (must be no lower than 1.5" below the top)
Vital Spark Logo (attached in pink and green)
Thrive Allies' Logo

BACK COVER REQUIREMENTS:
a place for summary text
thrive allies contact information
a place for an item # (can be small, no barcode)
Nice to have
• the colors i chose are samples, does not need to include every color, each title we write will have a different color story

I can appreciate a white cover with some amazing art of pops of color, but i would also love a really rich color with subtle tone on tone things (see the navy blue cover picture)
Should not have
• boring colors, lots of pictures, typical booklet design

```html
<!DOCTYPE html>
<html lang="en">
<head>
<meta charset="utf-8">
<title>Type 2 Diabetes — Vital Spark Primers Cover Spread</title>
<link rel="stylesheet" href="https://fonts.googleapis.com/css2?family=Oswald:wght@300;400&family=Roboto+Condensed:wght@400;700&family=Open+Sans:wght@400;600&display=swap">
<style>
  :root {
    --teal: #00a98f;
    --lime: #9bcb3c;
    --brand-green: #7cbf3f;
    --sun: #ffc214;
    --leaf: #9bcb3c;
    --tangerine: #f78f20;
    --white: #ffffff;
    --ink: #1a1a1a;
    --slate: #9a9a9a;
    --tag: #b3b3b3;
  }
  html, body {
    margin: 0;
    padding: 0;
    width: 1200px;
    height: 933px;
    overflow: hidden;
    background: var(--white);
  }
  .spread {
    position: relative;
    width: 1200px;
    height: 933px;
    overflow: hidden;
    font-family: "Open Sans", sans-serif;
  }

  /* ---------- Back cover ---------- */
  .back-cover {
    position: absolute;
    left: 0; top: 0;
    width: 600px; height: 933px;
    background: var(--white);
  }
  .back-cover__band {
    position: absolute;
    left: 0; top: 0;
    width: 600px; height: 583px;
    background: var(--teal);
  }
  .summary-box {
    position: absolute;
    left: 68px; top: 290px;
    width: 253px; height: 327px;
    background: var(--lime);
    box-sizing: border-box;
    padding: 31px 15px 0 17px;
  }
  .summary-box__text {
    margin: 0;
    font-family: "Roboto Condensed", sans-serif;
    font-size: 10.6px;
    line-height: 11.3px;
    color: var(--ink);
    text-align: justify;
  }
  .back-brand {
    position: absolute;
    left: 68px; top: 744px;
    display: flex;
    align-items: center;
    gap: 8px;
  }
  .back-brand__mark {
    width: 58px; height: 58px;
    border-radius: 10px;
    background: var(--slate);
  }
  .back-brand__name {
    font-family: "Open Sans", sans-serif;
    font-weight: 600;
    font-size: 20px;
    color: var(--slate);
  }
  .contact {
    position: absolute;
    left: 68px; top: 814px;
    font-family: "Roboto Condensed", sans-serif;
    font-size: 10.5px;
    line-height: 13px;
    color: var(--ink);
  }
  .contact__title { font-weight: 700; }
  .item-number {
    position: absolute;
    left: 478px; top: 850px;
    width: 62px; height: 19px;
    background: var(--tag);
    font-family: "Roboto Condensed", sans-serif;
    font-size: 10px;
    line-height: 19px;
    text-align: center;
    color: var(--ink);
  }

  /* ---------- Front cover ---------- */
  .front-cover {
    position: absolute;
    left: 600px; top: 0;
    width: 600px; height: 933px;
    background: var(--white);
  }
  .front-cover__band {
    position: absolute;
    left: 0; top: 579px;
    width: 600px; height: 354px;
    background: var(--teal);
  }
  .series-brand {
    position: absolute;
    left: 0; top: 66px;
    width: 600px;
    display: flex;
    flex-direction: column;
    align-items: center;
    gap: 6px;
  }
  .series-brand__dot {
    width: 40px; height: 40px;
    border-radius: 50%;
    background: var(--brand-green);
  }
  .series-brand__name {
    font-family: "Open Sans", sans-serif;
    font-weight: 600;
    font-size: 26px;
    line-height: 30px;
    color: var(--brand-green);
  }
  .numeral-art {
    position: absolute;
    left: 161px; top: 192px;
    width: 284px; height: 337px;
  }
  .title {
    margin: 0;
    font-family: "Oswald", sans-serif;
    font-weight: 300;
    color: var(--teal);
  }
  .title__type {
    position: absolute;
    left: 157px; top: 292px;
    font-size: 50px;
    line-height: 56px;
    letter-spacing: 0.5px;
  }
  .title__disease {
    position: absolute;
    left: 157px; top: 516px;
    font-size: 68px;
    line-height: 72px;
    letter-spacing: 1px;
  }
  .subtitle {
    position: absolute;
    left: 0; top: 584px;
    width: 600px;
    margin: 0;
    text-align: center;
    font-family: "Roboto Condensed", sans-serif;
    font-weight: 700;
    font-size: 17px;
    line-height: 25px;
    color: var(--white);
  }
  .values {
    position: absolute;
    left: 0; top: 704px;
    width: 600px;
    margin: 0;
    text-align: center;
    font-family: "Open Sans", sans-serif;
    font-weight: 400;
    font-size: 45px;
    line-height: 60px;
    letter-spacing: -1px;
  }
  .values__word--inspire { color: var(--sun); }
  .values__word--equip { color: var(--leaf); }
  .values__word--succeed { color: var(--tangerine); }
  .front-brand {
    position: absolute;
    left: 0; top: 808px;
    width: 600px;
    display: flex;
    justify-content: center;
    align-items: center;
    gap: 8px;
  }
  .front-brand__mark {
    width: 50px; height: 50px;
    border-radius: 9px;
    background: var(--white);
  }
  .front-brand__name {
    font-family: "Open Sans", sans-serif;
    font-weight: 600;
    font-size: 20px;
    color: var(--white);
  }
</style>
</head>
<body>
<main class="spread">

  <section class="back-cover">
    <div class="back-cover__band"></div>

    <div class="summary-box">
      <p class="summary-box__text">Type 2 diabetes affects millions of adults, yet many people live well with it every day. This simple guide walks you through what happens in your body when blood sugar rises, why it matters, and how small daily choices can make a real difference. Inside you will find clear explanations of testing, meals, movement, medicine and sleep, along with easy charts and practical tips you can start using right away. Learn how to read your numbers, plan balanced plates, shop with confidence and stay active at any age. We also share ways to manage stress, work with your care team and set goals that feel realistic. Whether you were just diagnosed or have been managing diabetes for years, this primer gives you the tools to take charge of your health, feel your best and keep moving forward one step at a time.</p>
    </div>

    <div class="back-brand">
      <div class="back-brand__mark"></div>
      <span class="back-brand__name">TA</span>
    </div>

    <address class="contact" style="font-style: normal;">
      <div class="contact__title">thrive allies contact information</div>
      <div>1250 Orchard Way, Suite 300</div>
      <div>Maple Falls, IA 50309</div>
      <div>(515) 555-0142 &nbsp;|&nbsp; info@thriveallies.example</div>
    </address>

    <div class="item-number">item #</div>
  </section>

  <section class="front-cover">
    <div class="front-cover__band"></div>

    <div class="series-brand">
      <div class="series-brand__dot"></div>
      <span class="series-brand__name">vital spark</span>
    </div>

    <svg class="numeral-art" viewBox="0 0 284 337" role="img" aria-label="Large numeral 2 built from an arrangement of colourful healthy foods: fruit, vegetables, grains, nuts and fish">
      <defs>
        <linearGradient id="foodTones" x1="0" y1="0" x2="1" y2="1">
          <stop offset="0" stop-color="#c98a4b"/>
          <stop offset="0.3" stop-color="#e0664a"/>
          <stop offset="0.55" stop-color="#b5c66a"/>
          <stop offset="0.8" stop-color="#d9a35a"/>
          <stop offset="1" stop-color="#8fb04a"/>
        </linearGradient>
      </defs>
      <path fill="url(#foodTones)" d="M18,100 C18,38 74,0 144,0 C218,0 268,46 268,112 C268,166 232,202 182,246 L124,298 L274,298 L274,337 L12,337 L12,298 L150,176 C196,136 214,120 214,104 C214,70 186,44 146,44 C106,44 78,70 76,108 Z"/>
    </svg>

    <h1 class="title">
      <span class="title__type">TYPE</span>
      <span class="title__disease">DIABETES</span>
    </h1>

    <p class="subtitle">A Simple Guide to Understanding &amp;<br>Controlling Your Blood Sugar</p>

    <p class="values">
      <span class="values__word--inspire">inspire</span>
      <span class="values__word--equip">equip</span>
      <span class="values__word--succeed">succeed</span>
    </p>

    <div class="front-brand">
      <div class="front-brand__mark"></div>
      <span class="front-brand__name">TA</span>
    </div>
  </section>

</main>
</body>
</html>
```